Beautiful Upgraded Single Story Home in Brindlemere...SOLD in 3 days for top $$!

This is a 6.5" x 11" EDDM postcard. Please use the indicia files and 6.5" x 11" template attached in the brief.
Updates

Project Deadline Extended
Reason: We are still working on the details for one of the postcards. Thanks

Target Market(s)

Listings

Font styles to use
Serif

Colors
33b8a4

Requirements
Must have
• Call me if you are interested in getting the most amount of equity out of your home!
• Marisol Pendry (555) 417-2963 and Tamsin Okavell (555) 730-4186
• Marisol@TeamOkavell.example and Tamsin@TeamOkavell.example
• Harbor Ridge Homes
• The Key to your Real Estate Needs!
• (At bottom of postcard) "If you are currently listed with a licensed Realtor, this is not intended as solicitation"
Nice to have
• The Front Should be the Property Picture and "In Escrow in 3 Days!"

```html
<!DOCTYPE html>
<html lang="en">
<head>
<meta charset="utf-8">
<title>Harbor Ridge Homes – Sold in 3 Days Postcard</title>
<link href="https://fonts.googleapis.com/css2?family=Roboto+Condensed:ital,wght@0,400;0,700;0,900;1,700;1,900&display=swap" rel="stylesheet">
<style>
  :root {
    --stage: #1d5b89;
    --teal: #33b8a4;
    --red: #e8232a;
    --white: #ffffff;
    --ink: #1f2a30;
    --sky-top: #7d8cc2;
    --sky-mid: #a7abd6;
    --dusk: #d9a6a0;
    --house: #5f6f8c;
    --street: #b7bccb;
    --logo-bg: #efece6;
  }
  * { margin: 0; padding: 0; box-sizing: border-box; }
  html, body { width: 1200px; height: 1200px; overflow: hidden; }
  body {
    background: var(--stage);
    font-family: "Roboto Condensed", "Arial Narrow", sans-serif;
    position: relative;
  }
  .card { position: absolute; overflow: hidden; }
  .card--front { left: 112px; top: 178px; width: 486px; height: 871px; }
  .card--back { left: 654px; top: 218px; width: 478px; height: 862px; background: var(--white); }
  .abs { position: absolute; }
  .center-line { left: 0; width: 100%; text-align: center; }

  .front-scene {
    inset: 0;
    background: linear-gradient(180deg, var(--sky-top) 0%, var(--sky-mid) 48%, var(--dusk) 64%, var(--house) 72%, var(--house) 86%, var(--street) 100%);
  }
  .headline-small { color: var(--white); font-weight: 400; font-size: 48px; line-height: 1; }
  .headline-big { color: var(--white); font-weight: 900; font-size: 82px; line-height: 1; }
  .subhead { color: var(--white); font-size: 24px; line-height: 1.3; text-transform: uppercase; }

  .stripe { position: absolute; height: 52px; background:
      linear-gradient(180deg, var(--red) 0 30%, transparent 30% 40%, var(--red) 40% 70%, transparent 70% 80%, var(--red) 80% 100%); }

  .sold {
    color: var(--red); font-weight: 900; font-style: italic; font-size: 100px; line-height: 1;
    -webkit-text-stroke: 3px var(--white); paint-order: stroke fill;
    text-shadow: 4px 4px 0 rgba(0,0,0,.35);
  }
  .sold-tag { color: var(--white); font-weight: 900; font-style: italic; font-size: 35px; white-space: nowrap; }

  .brand-box {
    background: var(--logo-bg);
    border: 4px solid var(--ink);
    outline: 4px solid var(--white);
    display: flex; align-items: center; justify-content: center; gap: 10px;
  }
  .brand-mark { width: 22px; height: 22px; background: var(--ink); flex: none; }
  .brand-name { color: var(--ink); font-weight: 700; font-size: 30px; line-height: 1.05; text-align: center; }

  .contact-front { color: var(--white); font-weight: 700; font-style: italic; font-size: 21px; line-height: 1.35;
    text-shadow: 1px 1px 2px rgba(0,0,0,.8); text-transform: uppercase; }

  .back-photo {
    left: 150px; top: 90px; width: 328px; height: 450px;
    background: linear-gradient(100deg, var(--white) 0%, #d8d8d8 30%, #3a3d44 55%, #2b2e35 100%);
  }
  .back-headline { color: var(--teal); font-size: 32px; white-space: nowrap; }
  .back-headline strong { font-weight: 900; font-size: 50px; }
  .for-top { color: var(--teal); font-weight: 900; font-style: italic; font-size: 38px; white-space: nowrap;
    -webkit-text-stroke: 2px var(--ink); paint-order: stroke fill; }
  .back-panel { left: 0; top: 540px; width: 100%; height: 322px; background: var(--teal); }
  .call-me { color: var(--white); font-weight: 700; font-size: 21px; line-height: 1.28; text-transform: uppercase; }
  .contact-back { color: var(--white); font-size: 21px; line-height: 1.25; text-transform: uppercase; }
  .disclaimer { color: var(--ink); font-weight: 700; font-size: 12.5px; line-height: 1.3; text-transform: uppercase; }
</style>
</head>
<body>

<section class="card card--front">
  <div class="abs front-scene" role="img" aria-label="Photo of a two-storey craftsman home at dusk with lit windows, garage and wet driveway"></div>

  <p class="abs center-line headline-small" style="top:34px;">In Escrow in</p>
  <p class="abs center-line headline-big" style="top:86px;">3 DAYS!</p>
  <p class="abs center-line subhead" style="top:170px;">Beautiful Upgraded<br>Single Story Home<br>in Brindlemere</p>

  <div class="stripe" style="left:-10px; top:320px; width:122px; transform:rotate(-4deg);"></div>
  <div class="stripe" style="left:384px; top:278px; width:115px; transform:rotate(-4deg);"></div>
  <p class="abs sold" style="left:130px; top:262px; transform:rotate(-6deg);">SOLD</p>
  <p class="abs sold-tag" style="left:72px; top:360px; transform:rotate(-7deg);">IN 3 DAYS FOR TOP $$!</p>

  <div class="abs brand-box" style="left:118px; top:658px; width:255px; height:119px;">
    <span class="brand-mark"></span>
    <span class="brand-name">Harbor Ridge<br>Homes</span>
  </div>

  <p class="abs center-line contact-front" style="top:786px;">Marisol Pendry (555) 417-2963<br>and Tamsin Okavell (555) 730-4186</p>
</section>

<section class="card card--back">
  <div class="abs back-photo" role="img" aria-label="Photo of a businessman in a dark suit holding a small model house in his palm"></div>

  <p class="abs center-line back-headline" style="top:34px;">In Escrow in <strong>3 DAYS!</strong></p>

  <div class="stripe" style="left:-10px; top:132px; width:122px; transform:rotate(-4deg);"></div>
  <div class="stripe" style="left:378px; top:94px; width:110px; transform:rotate(-4deg);"></div>
  <p class="abs sold" style="left:132px; top:82px; transform:rotate(-6deg);">SOLD</p>
  <p class="abs for-top" style="left:188px; top:180px; transform:rotate(-8deg);">FOR TOP $$!</p>

  <div class="abs back-panel"></div>

  <div class="abs brand-box" style="left:114px; top:484px; width:248px; height:115px;">
    <span class="brand-mark"></span>
    <span class="brand-name">Harbor Ridge<br>Homes</span>
  </div>

  <p class="abs center-line call-me" style="top:648px;">Call me if you are interested in<br>getting the most amount of<br>equity out of your home!</p>
  <p class="abs center-line contact-back" style="top:732px;">Marisol Pendry (555) 417-2963<br>and Tamsin Okavell (555) 730-4186</p>
  <p class="abs center-line disclaimer" style="top:797px;">If you are currently listed with a licensed Realtor,<br>this is not intended as solicitation"</p>
</section>

</body>
</html>
```